small auto electrical company needs new logo and business cards !!!

we are a small auto electrical company (Corvanne Motors Ltd) that has been running for 13 years the logo we have was put together by dinosaurs so we are looking at re branding the company starting with business cards and a new logo we fit GPS tracking devices for young drivers through there insurance company also we fit hands free systems and dash cameras also safety locks to fleet vehicles we would like bright eye catching colours day glow and neon and quirky designs for the logo our original logo was baby blue which i have added a picture enclosed we would like double sided but have a space to write notes and prices preferably not white on back same colour throughout many thanks
Reason: Just a chance to finalise any designs we want CM logos or C logos - No 1st's and no dinosaurs lol
Industry/Entity Type
Business
Contact Information for Business Card
Installs@corvannemotors.co.uk
07700900482
www.Corvannemotors.co.uk
Logo Text
Corvanne Motors Ltd - Fleets and Insurance Services
Requirements
Must have
- new logo design !!
Nice to have
- Satellite in logo or something attaining to gps
- maybe a car in the logo
Should not have
- shouldnt have first as 1st it is CoRVANNE Motors

```html
<!DOCTYPE html>
<html lang="en">
<head>
<meta charset="utf-8">
<title>Corvanne Motors Ltd – Business Card</title>
<link href="https://fonts.googleapis.com/css2?family=Ubuntu:wght@300;400;500&display=swap" rel="stylesheet">
<style>
  :root {
    --backdrop: #e4e4e4;
    --card: #ffffff;
    --brand-blue: #00a8e8;
    --band-grey: #939598;
    --ink: #2b2b2b;
    --ink-soft: #5c5c5c;
    --ghost: #efefef;
    --icon-bg: #ffffff;
  }
  * { box-sizing: border-box; margin: 0; padding: 0; }
  html, body { width: 1200px; height: 900px; overflow: hidden; }
  body {
    background: var(--backdrop);
    font-family: "Ubuntu", sans-serif;
    display: flex;
    align-items: center;
    justify-content: center;
    gap: 40px;
  }
  .card {
    position: relative;
    width: 540px;
    height: 340px;
    background: var(--card);
    overflow: hidden;
    box-shadow: 0 6px 18px rgba(0,0,0,0.12);
  }

  /* ---------- Front ---------- */
  .name-band {
    position: absolute;
    left: 0; top: 62px;
    width: 262px; height: 46px;
    background: var(--band-grey);
    border-top-right-radius: 22px;
    color: #fff;
    padding: 6px 0 0 26px;
  }
  .name-band .person { font-weight: 300; font-size: 20px; line-height: 1.1; }
  .name-band .role { font-weight: 300; font-size: 11px; }

  .contact-band {
    position: absolute;
    left: 0; top: 108px;
    width: 270px; height: 112px;
    background: var(--brand-blue);
    padding: 12px 0 0 22px;
    list-style: none;
  }
  .contact-band li {
    display: flex;
    align-items: flex-start;
    gap: 7px;
    color: var(--ink);
    font-size: 14.5px;
    line-height: 1.05;
    margin-bottom: 6px;
  }
  .contact-band li.address { font-size: 11.5px; }
  .contact-icon {
    flex: none;
    width: 14px; height: 14px;
    border-radius: 50%;
    background: var(--icon-bg);
    display: flex; align-items: center; justify-content: center;
  }
  .contact-icon svg { width: 9px; height: 9px; }

  .foot-block {
    position: absolute;
    right: 0; bottom: 0;
    width: 270px; height: 74px;
    background: var(--brand-blue);
  }

  .brand {
    position: absolute;
    left: 270px; top: 70px;
    width: 270px;
    display: flex;
    flex-direction: column;
    align-items: center;
    text-align: center;
  }
  .brand-dot {
    width: 58px; height: 58px;
    border-radius: 50%;
    background: var(--brand-blue);
    margin-bottom: 18px;
  }
  .brand-name {
    color: var(--brand-blue);
    font-weight: 500;
    font-size: 22px;
    letter-spacing: 0.5px;
    text-transform: uppercase;
  }
  .brand-tagline {
    color: var(--ink-soft);
    font-weight: 400;
    font-size: 10.5px;
    letter-spacing: 1.4px;
    text-transform: uppercase;
    margin-top: 4px;
  }

  /* ---------- Back ---------- */
  .ghost-ring {
    position: absolute;
    left: 210px; top: 26px;
    width: 120px; height: 120px;
    border-radius: 50%;
    background: var(--ghost);
  }
  .back-brand {
    position: absolute;
    left: 0; top: 170px;
    width: 100%;
    text-align: center;
  }
  .back-brand .brand-name { font-size: 26px; }
  .back-brand .brand-tagline { font-size: 12px; }
  .back-bar {
    position: absolute;
    right: 0; top: 250px;
    width: 130px; height: 16px;
    background: var(--brand-blue);
  }
  .back-bar-left {
    position: absolute;
    left: 0; top: 250px;
    width: 130px; height: 16px;
    background: var(--brand-blue);
  }
</style>
</head>
<body>

  <section class="card card-front" aria-label="Business card front">
    <div class="name-band">
      <p class="person">Xxxxx Xxxxxx</p>
      <p class="role">Director</p>
    </div>

    <ul class="contact-band">
      <li>
        <span class="contact-icon"><svg viewBox="0 0 10 10"><rect x="1" y="2.5" width="8" height="5.5" fill="none" stroke="#2b2b2b" stroke-width="1"/><path d="M1 2.5 L5 6 L9 2.5" fill="none" stroke="#2b2b2b" stroke-width="1"/></svg></span>
        Installs@corvannemotors.co.uk
      </li>
      <li>
        <span class="contact-icon"><svg viewBox="0 0 10 10"><rect x="3" y="1" width="4" height="8" rx="0.8" fill="none" stroke="#2b2b2b" stroke-width="1"/><circle cx="5" cy="7.5" r="0.5" fill="#2b2b2b"/></svg></span>
        07700900482
      </li>
      <li>
        <span class="contact-icon"><svg viewBox="0 0 10 10"><circle cx="5" cy="5" r="4" fill="none" stroke="#2b2b2b" stroke-width="0.9"/><ellipse cx="5" cy="5" rx="1.8" ry="4" fill="none" stroke="#2b2b2b" stroke-width="0.8"/><path d="M1 5 H9" stroke="#2b2b2b" stroke-width="0.8"/></svg></span>
        www.Corvannemotors.co.uk
      </li>
      <li class="address">
        <span class="contact-icon"><svg viewBox="0 0 10 10"><path d="M1 5 L5 1.5 L9 5 H7.5 V9 H2.5 V5 Z" fill="#2b2b2b"/></svg></span>
        xxx xxxxxx xxxxx xxx<br>xxxx
      </li>
    </ul>

    <div class="brand">
      <span class="brand-dot"></span>
      <p class="brand-name">Corvanne Motors Ltd</p>
      <p class="brand-tagline">Fleet &amp; Insurance Services</p>
    </div>

    <div class="foot-block"></div>
  </section>

  <section class="card card-back" aria-label="Business card back">
    <span class="ghost-ring"></span>
    <div class="back-brand">
      <p class="brand-name">Corvanne Motors Ltd</p>
      <p class="brand-tagline">Fleet &amp; Insurance Services</p>
    </div>
    <div class="back-bar"></div>
  </section>

</body>
</html>
```